Redesign of existing site - Velbrin GmbH

Redesign of the following site.
https://www.velbrin-gmbh.example/

The colors red and green need to remain.
Topic: calendar binder

The font "FF Market Regular" should be used s well. But -- if you find a font which is similar and a bit more modern, then go with it. (see font-example.jpg)

The mainpage should have a slider with a video first. Enclosed is a screenshot of the video. (see video.jpg)

Logo also enclosed as svg. The red color might not be quit right. Please check it on your own.
For the second page this page should be used to redesign:
https://www.velbrin-gmbh.example/bindungen/ring-wire-bindung/

I am planing to use the DIVI builder. If you built this in DIVI builder and be able to send me the template or installation (Duplicator) that would be a huge advantage.
Updates

IMPORTANT:
I have received many designs in English. But I can't present them to the customer. Please convert them into German, otherwise they cannot be used.

Requirements
Must have
• Please translate designs into german if it is to be considered. How should I explain a design in english to the customer?

```html
<!DOCTYPE html>
<html lang="de">
<head>
<meta charset="utf-8">
<title>Velbrin GmbH – Zuverlässige Drahtbindung</title>
<link href="https://fonts.googleapis.com/css2?family=Inter:wght@400;500;600;700;800&family=Kaushan+Script&display=swap" rel="stylesheet">
<style>
:root{
  --red:#d0101c;
  --green:#2e8b3e;
  --ink:#111111;
  --text:#2a2a2a;
  --muted:#6b6b6b;
  --line:#dcdcdc;
  --pink:#fdf0f0;
  --white:#ffffff;
  --black:#000000;
  --star:#f5b400;
}
*{box-sizing:border-box;margin:0;padding:0}
html,body{width:1200px;height:4528px;overflow:hidden}
body{position:relative;background:var(--white);font-family:"Inter",sans-serif;color:var(--text)}
.abs{position:absolute}
.script{font-family:"Kaushan Script",cursive;color:var(--ink);font-weight:400}
.eyebrow{font-size:19px;font-weight:500;color:var(--ink)}
.btn{position:absolute;display:flex;align-items:center;justify-content:center;gap:6px;border-radius:20px;font-size:11px;font-weight:600;color:var(--white);text-transform:uppercase;letter-spacing:.2px;white-space:nowrap}
.btn-red{background:var(--red)}
.btn-dark{background:var(--ink)}
.wordmark{font-family:"Inter",sans-serif;font-weight:800;color:var(--red);letter-spacing:-1px;line-height:1}

/* header */
.site-header{position:absolute;left:0;top:0;width:1200px;height:86px;background:var(--white);border-bottom:3px solid var(--green)}
.site-header .wordmark{position:absolute;left:150px;top:27px;font-size:30px}
.main-nav{position:absolute;left:365px;top:35px;display:flex;gap:24px;font-size:12.5px;color:var(--ink);font-weight:500;white-space:nowrap}
.main-nav .active{color:var(--red)}

/* hero */
.hero{position:absolute;left:0;top:86px;width:1200px;height:543px;background:linear-gradient(100deg,#dfe7ea 0%,#cfdde2 35%,#9fc4cf 60%,#2aa6be 82%,#1a8ea8 100%)}
.hero h1{position:absolute;left:151px;top:148px;font-size:35px;line-height:52px}
.hero p{position:absolute;left:151px;top:270px;width:370px;font-size:12.5px;line-height:19px;color:var(--ink)}
.play{position:absolute;left:991px;top:242px;width:60px;height:60px;border-radius:50%;background:rgba(255,255,255,.85)}

/* about */
.about-img{left:153px;top:724px;width:439px;height:357px;background:linear-gradient(135deg,#f3f4f8,#d9dde6 50%,#f1c9c9)}
.about-small{left:838px;top:944px;width:157px;height:128px;background:linear-gradient(160deg,#9a9a9a,#4a4a4a);border-radius:2px}
.about-copy{left:659px;width:360px;font-size:12px;line-height:18px;color:var(--text)}

/* stats */
.stats{left:149px;top:1175px;width:902px;height:113px;border:1px solid var(--line);border-top:2px solid var(--green);display:flex;align-items:center}
.stat{flex:1;text-align:center;border-right:1px solid #bbb;height:46px;display:flex;flex-direction:column;justify-content:center}
.stat:last-child{border-right:none}
.stat b{font-size:16px;font-weight:700;color:var(--ink)}
.stat span{font-size:10px;color:var(--ink);margin-top:4px;line-height:12px}
.stat.hl b,.stat.hl span{color:var(--red)}

/* steps */
.step-icon{position:absolute;left:168px;width:34px;height:34px;border-radius:50%;background:var(--white);border:2px solid var(--green);box-shadow:0 2px 8px rgba(0,0,0,.15)}
.step-icon.on{background:var(--red);border-color:var(--red)}
.step-title{position:absolute;left:220px;font-size:16px;font-weight:500;color:var(--ink)}
.step-text{position:absolute;left:220px;width:270px;font-size:12.5px;line-height:20px;color:var(--muted)}

/* feature cards */
.feature{position:absolute;top:2038px;width:211px;height:251px;text-align:center}
.feature h3{font-size:15px;font-weight:500;color:var(--ink);line-height:20px}
.feature p{font-size:12.5px;line-height:20px;color:var(--muted);padding:0 18px;margin-top:20px}

/* products */
.product{position:absolute;top:2546px;width:211px;text-align:center}
.product .ph{height:198px;border-radius:4px}
.product h3{margin-top:33px;font-size:16px;font-weight:500;color:var(--ink)}
.product .desc{margin-top:8px;font-size:11px;line-height:16px;color:var(--muted);padding:0 6px}
.product .sizes{margin-top:10px;font-size:11px;font-weight:500;color:var(--ink)}
.product .btn{position:relative;margin:12px auto 0;width:178px;height:40px;font-size:10px}

/* gallery */
.gal{position:absolute;border-radius:3px}

/* testimonials */
.quote{position:absolute;top:3820px;width:445px;height:183px;border:1px solid var(--line);border-radius:8px;text-align:center}
.quote p{margin:58px 30px 0;font-size:9.5px;line-height:13px;color:var(--muted)}
.stars{margin-top:12px;display:flex;justify-content:center;gap:8px}
.avatar{position:absolute;top:3780px;width:84px;height:84px;border-radius:50%;border:2px solid #e8a0a0;background:linear-gradient(180deg,#e6eef4,#9fb0c2)}

/* footer */
.site-footer{position:absolute;left:0;top:4097px;width:1200px;height:431px;background:var(--black);color:var(--white);border-top:4px solid var(--green)}
.site-footer .wordmark{position:absolute;left:160px;top:136px;font-size:40px}
.foot-col{position:absolute;top:125px;font-size:12px;line-height:16px}
.foot-col h4{font-size:12px;font-weight:700;margin-bottom:14px}
.foot-col a{display:block;color:var(--white);text-decoration:none;margin-bottom:18px}
.social{position:absolute;top:4403px;width:28px;height:28px;border-radius:6px;background:var(--white)}
</style>
</head>
<body>

<header class="site-header">
  <div class="wordmark">VELBRIN</div>
  <nav class="main-nav">
    <span class="active">STARTSEITE</span><span>ÜBER UNS</span><span>PRODUKTE ▾</span><span>SO FUNKTIONIERT'S</span><span>GALERIE</span>
  </nav>
  <a class="btn btn-red" style="left:921px;top:25px;width:130px;height:37px;">Kontakt ↗</a>
</header>

<section class="hero" role="img" aria-label="Nahaufnahme eines drahtgebundenen Notizbuchs mit blauem Umschlag">
  <h1 class="script">Zuverlässige Drahtbindung für<br>Kalender &amp; mehr</h1>
  <p>Lorem Ipsum Dolor Sit Amet, Consectetur Adipiscing Elit, Sed Do Eiusmod Tempor Incididunt Ut Labore Et Dolore Magna Aliqua. Ut Enim Ad Minim</p>
  <a class="btn btn-red" style="left:150px;top:353px;width:190px;height:36px;">Kostenloses Angebot ↗</a>
  <div class="play"><svg width="60" height="60" viewBox="0 0 60 60"><path d="M25 21 L39 30 L25 39 Z" fill="#111"/></svg></div>
</section>

<!-- about -->
<div class="abs about-img" role="img" aria-label="Foto gestapelter drahtgebundener Notizbücher"></div>
<div class="abs eyebrow" style="left:659px;top:736px;">Über uns</div>
<h2 class="abs script" style="left:659px;top:772px;font-size:27px;line-height:45px;">Gebaut auf Erfahrung. Getrieben<br>von Präzision</h2>
<p class="abs about-copy" style="top:886px;">Lorem Ipsum Dolor Sit Amet, Consectetur Adipiscing Elit, Sed Do Eiusmod Tempor Incididunt Ut Labore Et Dolore Magna Aliqua. Ut Enim Ad Minim</p>
<div class="abs" style="left:659px;top:964px;display:flex;align-items:center;gap:6px;">
  <b style="color:var(--red);font-size:17px;">30+</b>
  <span style="font-size:10px;line-height:12px;color:var(--ink);">Jahre Erfahrung in<br>Bindelösungen</span>
</div>
<a class="btn btn-red" style="left:659px;top:1016px;width:130px;height:35px;">Weiterlesen ↗</a>
<div class="abs about-small" role="img" aria-label="Foto eines schwarzen Tischkalenders mit Ringbindung"></div>

<!-- stats -->
<div class="abs stats">
  <div class="stat"><b>30+</b><span>Jahre<br>Erfahrung</span></div>
  <div class="stat"><b>50.000+</b><span>Projekte<br>abgeschlossen</span></div>
  <div class="stat hl"><b>2.000+</b><span>Zufriedene Kunden</span></div>
  <div class="stat"><b>12+</b><span>Zufriedene Kunden</span></div>
  <div class="stat"><b>15</b><span><strong>Hochleistungs-<br>maschinen</strong></span></div>
</div>

<!-- how it works -->
<div class="abs eyebrow" style="left:167px;top:1378px;">So funktioniert's</div>
<h2 class="abs script" style="left:167px;top:1411px;font-size:27px;line-height:43px;">Von der Idee bis zur Lieferung<br>Ganz ohne Aufwand</h2>
<svg class="abs" style="left:184px;top:1560px;" width="2" height="260"><line x1="1" y1="0" x2="1" y2="260" stroke="var(--green)" stroke-opacity=".5" stroke-width="2"/></svg>
<div class="step-icon" style="top:1540px;"></div>
<div class="step-title" style="top:1533px;">Produktionsstart</div>
<p class="step-text" style="top:1565px;">Lorem Ipsum Dolor Sit Amet, Consectetur Adipiscing Elit, Sed Do Eiusmod Tempor</p>
<div class="step-icon on" style="top:1672px;"></div>
<div class="step-title" style="top:1665px;">Qualitätskontrolle</div>
<p class="step-text" style="top:1697px;">Lorem Ipsum Dolor Sit Amet, Consectetur Adipiscing Elit, Sed Do Eiusmod Tempor</p>
<div class="step-icon" style="top:1810px;"></div>
<div class="step-title" style="top:1804px;">Schnelle Lieferung</div>
<p class="step-text" style="top:1836px;">Lorem Ipsum Dolor Sit Amet, Consectetur Adipiscing Elit, Sed Do Eiusmod Tempor</p>
<a class="btn btn-red" style="left:221px;top:1903px;width:140px;height:36px;">Mehr erfahren ↗</a>
<div class="abs" style="left:694px;top:1490px;width:343px;height:346px;background:linear-gradient(180deg,#fafafa,#e4e4e4);" role="img" aria-label="Foto einer weißen Drahtbindemaschine"></div>

<!-- features -->
<div class="feature" style="left:162px;background:var(--white);box-shadow:0 2px 10px rgba(0,0,0,.08);border-bottom:2px solid var(--red);">
  <svg style="margin-top:32px" width="60" height="56" viewBox="0 0 60 56" fill="none" stroke="#111" stroke-width="3"><circle cx="30" cy="14" r="8"/><circle cx="12" cy="40" r="5"/><circle cx="30" cy="40" r="5"/><circle cx="48" cy="40" r="5"/><path d="M30 22v13M30 28L14 36M30 28l16 8"/></svg>
  <h3 style="margin-top:18px">Unser Team</h3>
  <p>Lorem Ipsum Dolor Sit Amet Consectetur Adipiscing Sed Do Eiusmod</p>
</div>
<div class="feature" style="left:409px;background:var(--pink);">
  <svg style="margin-top:30px" width="66" height="62" viewBox="0 0 66 62" fill="none" stroke="#111" stroke-width="3"><rect x="8" y="6" width="42" height="36" rx="3"/><path d="M16 16h26M16 24h20M16 32h14"/><circle cx="46" cy="44" r="10"/><path d="M8 42l-4 12 14-8"/></svg>
  <h3 style="margin-top:10px;font-size:14px;">Technische<br>Informationen</h3>
  <p style="margin-top:16px">Lorem Ipsum Dolor Sit Amet Consectetur Adipiscing Sed Do Eiusmod</p>
</div>
<div class="abs wordmark" style="left:657px;top:2050px;font-size:34px;">VELBRIN</div>
<p class="abs" style="left:658px;top:2124px;width:278px;font-size:12.5px;line-height:20px;color:var(--muted);">Lorem Ipsum Dolor Sit Amet, Consectetur Adipiscing Elit, Sed Do Eiusmod Tempor Incididunt Ut Labore Et Dolore Magna Aliqua. Ut Enim Ad Minim Veniam, Quis Nostrud Exercitation Ullamco Laboris Nisi Ut Aliquip Ex Ea Commodo Consequat. Duis Aute Irure Dolor In Reprehenderit In Voluptate Velit Esse Cillum Dolore Eu Fugiat Nulla Pariatur.</p>

<!-- products -->
<div class="abs eyebrow" style="left:0;width:1180px;text-align:center;top:2384px;">Produkte</div>
<h2 class="abs script" style="left:0;width:1140px;text-align:center;top:2421px;font-size:27px;line-height:43px;">Stark, stilvoll, zuverlässig –<br>wie unsere Bindungen</h2>
<div class="product" style="left:123px;">
  <div class="ph" role="img" aria-label="Foto eines schwarzen Tischkalenders mit Ring-Wire-Bindung" style="background:linear-gradient(160deg,#bdbdbd,#5a5a5a);"></div>
  <h3>Ring-Wire-Bindung</h3><p class="desc">Eine stabile und elegante Drahtbindung, ideal</p><p class="sizes">Formate (A4, A5 usw.)</p>
  <a class="btn btn-dark">Alle Produktdetails</a>
</div>
<div class="product" style="left:360px;">
  <div class="ph" role="img" aria-label="Foto loser schwarzer Bindedrähte" style="background:linear-gradient(180deg,#ffffff,#ececec);"></div>
  <h3>Bindungszubehör</h3><p class="desc">Eine stabile und elegante Drahtbindung, ideal</p><p class="sizes">Formate (A4, A5 usw.)</p>
  <a class="btn btn-dark">Alle Produktdetails</a>
</div>
<div class="product" style="left:589px;">
  <div class="ph" role="img" aria-label="Foto gestapelter Notizbücher mit orangem Umschlag" style="background:linear-gradient(160deg,#e6e6e6,#f08a2c 55%,#6a6a6a);"></div>
  <h3>Bindedrähte</h3><p class="desc">Eine stabile und elegante Drahtbindung, ideal</p><p class="sizes">Formate (A4, A5 usw.)</p>
  <a class="btn btn-dark">Alle Produktdetails</a>
</div>
<div class="product" style="left:831px;">
  <div class="ph" role="img" aria-label="Foto eines weißen Tischkalenders" style="background:linear-gradient(160deg,#ffffff,#e8f1ee);border:1px solid var(--line);"></div>
  <h3>Kalenderaufhänger</h3><p class="desc">Eine stabile und elegante Drahtbindung, ideal</p><p class="sizes">Formate (A4, A5 usw.)</p>
  <a class="btn btn-dark">Alle Produktdetails</a>
</div>

<!-- gallery -->
<div class="abs eyebrow" style="left:0;width:1161px;text-align:center;top:3014px;">Galerie</div>
<h2 class="abs script" style="left:0;width:1168px;text-align:center;top:3050px;font-size:27px;">Handwerk sehen. Qualität spüren</h2>
<div class="gal" style="left:53px;top:3198px;width:160px;height:276px;background:linear-gradient(180deg,#f4f4f4,#c9c9c9);" role="img" aria-label="Foto eines Wandkalenders mit Brille"></div>
<div class="gal" style="left:206px;top:3163px;width:190px;height:346px;background:linear-gradient(180deg,#efefef,#e5e5e5 40%,#d8d8d8);" role="img" aria-label="Foto eines drahtgebundenen Kalenders mit rotem Kopf"></div>
<div class="gal" style="left:713px;top:3163px;width:227px;height:346px;background:linear-gradient(160deg,#f2f2f2,#e43b44 45%,#b8101c);" role="img" aria-label="Foto gestapelter roter drahtgebundener Notizbücher"></div>
<div class="gal" style="left:922px;top:3198px;width:192px;height:276px;background:linear-gradient(160deg,#8a8a8a,#e9e9e9 50%,#e8c27a);" role="img" aria-label="Foto eines hängenden Wandkalenders"></div>
<div class="gal" style="left:387px;top:3129px;width:326px;height:411px;background:linear-gradient(170deg,#d4d4d4,#8e8e8e 60%,#6a6a6a);box-shadow:0 4px 14px rgba(0,0,0,.2);" role="img" aria-label="Foto eines schwarzen ringgebundenen Tischkalenders"></div>
<svg class="abs" style="left:547px;top:3562px;" width="72" height="22" viewBox="0 0 72 22" fill="none" stroke-width="2.5"><path d="M30 11H3M11 3L3 11l8 8" stroke="#111"/><path d="M42 11h27M61 3l8 8-8 8" stroke="var(--red)"/></svg>

<!-- testimonials -->
<div class="abs eyebrow" style="left:0;width:1208px;text-align:center;top:3662px;">Kundenstimmen</div>
<h2 class="abs script" style="left:0;width:1208px;text-align:center;top:3700px;font-size:26px;">Echte Menschen, echte Ergebnisse</h2>
<div class="quote" style="left:149px;">
  <p>Lorem ipsum dolor sit amet, consectetur adipiscing elit, sed do eiusmod tempor incididunt ut labore et dolore magna aliqua. Ut enim ad minim veniam, quis nostrud exercitation ullamco laboris nisi ut aliquip ex ea commodo consequat. Duis aute irure dolor in reprehenderit in voluptate .</p>
  <div class="stars">
    <svg width="150" height="24" viewBox="0 0 150 24" fill="var(--star)"><g id="star"><path d="M12 1l3.2 7 7.6.7-5.8 5 1.8 7.5L12 17.3 5.2 21.2 7 13.7 1.2 8.7l7.6-.7z"/></g><use href="#star" x="32"/><use href="#star" x="64"/><use href="#star" x="96"/><use href="#star" x="128"/></svg>
  </div>
</div>
<div class="quote" style="left:606px;">
  <p>Lorem ipsum dolor sit amet, consectetur adipiscing elit, sed do eiusmod tempor incididunt ut labore et dolore magna aliqua. Ut enim ad minim veniam, quis nostrud exercitation ullamco laboris nisi ut aliquip ex ea commodo consequat. Duis aute irure dolor in reprehenderit in voluptate .</p>
  <div class="stars">
    <svg width="150" height="24" viewBox="0 0 150 24" fill="var(--star)"><use href="#star" x="0"/><use href="#star" x="32"/><use href="#star" x="64"/><use href="#star" x="96"/><use href="#star" x="128"/></svg>
  </div>
</div>
<div class="avatar" style="left:323px;" role="img" aria-label="Porträtfoto eines Kunden"></div>
<div class="avatar" style="left:779px;" role="img" aria-label="Porträtfoto eines Kunden"></div>

<!-- footer -->
<footer class="site-footer">
  <div class="wordmark">VELBRIN</div>
  <p class="abs" style="left:160px;top:226px;width:260px;font-size:12px;line-height:19px;">Lorem Ipsum Dolor Sit Amet, Consectetur Adipiscing Elit, Sed Do Eiusmod Tempor Incididunt Ut Labore Et Dolore</p>
  <div class="foot-col" style="left:522px;">
    <h4>LINKS</h4>
    <a style="font-weight:700">STARTSEITE</a><a>ÜBER UNS</a><a>PRODUKTE</a><a>SO FUNKTIONIERT'S</a><a>GALERIE</a>
  </div>
  <div class="foot-col" style="left:717px;">
    <h4>RECHTLICHES</h4>
    <a>Impressum</a><a>Produkte</a><a style="font-size:11px">Cookie-Richtlinie</a><a>FAQ</a>
  </div>
  <p class="foot-col" style="left:887px;width:160px;font-size:12px;line-height:21px;">LOREM IPSUM DOLOR SIT AMET, CONSECTETUR ADIPISCING ELIT, SED DO EIUSMOD TEMPOR INCIDIDUNT UT LABORE ET DOLORE MAGNA ALIQUA. UT ENIM AD MINIM VENIAM, QUIS NOSTRUD EXERCITATION</p>
</footer>
<div class="social" style="left:160px;"></div>
<div class="social" style="left:200px;border-radius:50%;"></div>
<div class="social" style="left:238px;"></div>
<div class="social" style="left:276px;border-radius:50%;"></div>

</body>
</html>
```